Entertainment Sound and Lighting company Business card

We need a professional looking business card designed for my growing entertainment sound and lighting company based in Sydney, Australia called "Kestrel Sound"

We provide technical production services (sound systems/lighting/vision) for events ranging from band gigs, weddings, corporate functions etc.

The business card needs to contain the following information:

Bartholomew Quenneville
Audio Engineer
Phone: 0478 615 702
Email: bartholomew@kestrelsound.com.au
Website: www.kestrelsound.com.au

Business logo has been attached in .ai format, please contact me if you need me to provide other files.

Target Market(s)

We need a business card that reflects our modern and professional company but still looks professional to appeal to our corporate clients.
We have a very broad target market spanning from bands needing PA systems for their gigs (18-30yrs) to event companies needing sound and lighting for weddings and other functions.

Industry/Entity Type

Business

Requirements
Must have
• Needs to include the logo that is attached of course, and the colour scheme.
Nice to have
• - Double sided

```html
<!DOCTYPE html>
<html lang="en">
<head>
<meta charset="utf-8">
<title>Kestrel Sound — Business Card</title>
<link rel="stylesheet" href="https://fonts.googleapis.com/css2?family=Quicksand:wght@400;500;700&family=Noto+Sans:wght@400&family=PT+Sans+Narrow&display=swap">
<style>
  :root {
    --backdrop: #2c2e31;
    --cyan-light: #4ef0ea;
    --cyan-deep: #25b4ec;
    --white: #ffffff;
    --strip: #f4f5f5;
    --brand-blue: #1f84e2;
    --title-teal: #1c6c8c;
    --link-grey: #4a4f55;
    --paper: #e8e7e2;
    --paper-light: #f2f1ed;
    --tagline-grey: #6b6d70;
    --rule: #8e8f91;
  }
  * { box-sizing: border-box; margin: 0; padding: 0; }
  html, body {
    width: 945px; height: 1200px; overflow: hidden;
    background: var(--backdrop);
  }
  .card {
    position: absolute; left: 62px;
    width: 820px; height: 469px;
    overflow: hidden;
    box-shadow: 0 10px 30px rgba(0,0,0,.45);
  }
  /* Front side */
  .card--front {
    top: 70px;
    background: radial-gradient(ellipse 75% 80% at 45% 55%, var(--cyan-light) 0%, #3ad7ee 55%, var(--cyan-deep) 100%);
  }
  .corner-ribbon { position: absolute; left: 0; top: 0; width: 200px; height: 200px; }
  .ribbon-brand {
    position: absolute; left: 0; top: 0;
    width: 212px; text-align: center;
    font: 700 17px "Quicksand", sans-serif;
    color: var(--brand-blue);
    transform-origin: center;
    transform: translate(-32px, 64px) rotate(-45deg);
  }
  .identity { position: absolute; right: 60px; top: 168px; text-align: right; }
  .identity__name {
    font: 500 40px "Quicksand", sans-serif;
    color: var(--white); letter-spacing: .5px;
  }
  .identity__role {
    font: 24px "PT Sans Narrow", sans-serif;
    color: var(--title-teal); margin-top: -4px;
  }
  .contact {
    position: absolute; left: 405px; top: 318px;
    font: 19px/1.45 "Noto Sans", sans-serif;
    color: var(--white); letter-spacing: .3px;
  }
  .social-strip {
    position: absolute; left: 0; right: 0; bottom: 0; height: 34px;
    background: var(--strip);
    display: flex; justify-content: flex-end; align-items: center;
    padding-right: 40px; gap: 14px;
    font: 14px "Noto Sans", sans-serif; color: var(--link-grey);
  }
  .social-link { display: flex; align-items: center; gap: 7px; }
  .social-link__mark { width: 16px; height: 16px; background: var(--cyan-deep); }
  .social-divider { width: 1px; height: 18px; background: #c9cccf; }
  /* Back side */
  .card--back {
    top: 650px;
    background: radial-gradient(ellipse 70% 70% at 50% 40%, var(--paper-light) 0%, var(--paper) 100%);
  }
  .brand-block {
    position: absolute; left: 0; right: 0; top: 95px;
    display: flex; flex-direction: column; align-items: center;
  }
  .brand-mark { width: 34px; height: 34px; border-radius: 50%; background: var(--brand-blue); }
  .brand-name {
    font: 700 50px "Quicksand", sans-serif;
    color: var(--brand-blue); margin-top: 14px;
  }
  .brand-rule {
    width: 340px; height: 1px; margin-top: 10px;
    background: linear-gradient(90deg, transparent, var(--rule) 50%, transparent);
  }
  .tagline {
    margin-top: 30px; text-align: center;
    font: 400 36px/1.05 "Quicksand", sans-serif;
    color: var(--tagline-grey);
  }
</style>
</head>
<body>
  <section class="card card--front">
    <svg class="corner-ribbon" viewBox="0 0 200 200" aria-hidden="true">
      <polygon points="118,0 182,0 0,182 0,118" fill="#ffffff"/>
    </svg>
    <div class="ribbon-brand">Kestrel Sound</div>

    <div class="identity">
      <h1 class="identity__name">Bartholomew Quenneville</h1>
      <p class="identity__role">Audio Engineer</p>
    </div>

    <div class="contact">
      <p>Phone: 0478 615 702</p>
      <p>Email: bartholomew@kestrelsound.com.au</p>
      <p>Website: www.kestrelsound.com.au</p>
    </div>

    <div class="social-strip">
      <span class="social-link"><span class="social-link__mark"></span>www.lumenpage.com/kestrelsound</span>
      <span class="social-divider"></span>
      <span class="social-link"><span class="social-link__mark"></span>chirpline.com/kestrelsound</span>
    </div>
  </section>

  <section class="card card--back">
    <div class="brand-block">
      <span class="brand-mark"></span>
      <h2 class="brand-name">Kestrel Sound</h2>
      <span class="brand-rule"></span>
      <p class="tagline">“Entertainment sound<br>and<br>lighting company”</p>
    </div>
  </section>
</body>
</html>
```